Lumen Kinetics Web Design Project

We need to update our web design for our company. Lumen Kinetics™ is a series of Development (Training) Programs that we deliver both for the General Public as well as Corporate Business.

Much of the content needs a refresh but we are keen to get some thoughts now on design and layout, predominantly front page. Happy to take any comments on the content if you think that is relevant as well.

We might look to move the current video clip and bring a more generic 'inspirational' clip to the front page. A good example of this is www.mindcraftoz.example.au

Our courses have a very similar market to Gerald Whitcombe type courses ... both General Public and Corporate business.

Refer our website www.lumenkinetics.example.com

Target Market(s)

General Public as well as Corporate Business. Courses are designed for all. Gerald Whitcombe would be a good 'feel' for what we do.

Industry/Entity Type

Business

Requirements
Must have
• Must have a 'leading edge' type feel to it.
Must look professional.

```html
<!DOCTYPE html>
<html lang="en">
<head>
<meta charset="utf-8">
<title>Lumen Kinetics – Home</title>
<link href="https://fonts.googleapis.com/css2?family=Jost:wght@300;400;500&family=Open+Sans:wght@400;600;700&display=swap" rel="stylesheet">
<style>
:root{
  --navy:#263f8a;
  --navy-deep:#1c2f6f;
  --sky:#8fb1e8;
  --lime:#a6d14a;
  --lime-btn:#8fbe3a;
  --leaf:#84ad35;
  --leaf-dark:#2f5010;
  --grass:#6a9a1f;
  --grey-text:#6b6b6b;
  --white:#ffffff;
}
*{margin:0;padding:0;box-sizing:border-box}
html,body{width:934px;height:1200px;overflow:hidden;background:#fff}
body{font-family:"Open Sans",sans-serif;position:relative}
.page{position:relative;width:934px;height:1200px;overflow:hidden}
.abs{position:absolute}
.heading{font-family:"Jost",sans-serif}

/* header */
.hero{left:0;top:0;width:934px;height:398px;background:var(--navy)}
.zig-down{height:6px;width:934px;background:
  linear-gradient(135deg,var(--navy) 50%,transparent 50%) 0 0/8px 6px,
  linear-gradient(225deg,var(--navy) 50%,transparent 50%) 0 0/8px 6px;}
.brand{left:142px;top:14px;color:var(--white);font-family:"Open Sans",sans-serif;font-weight:400;font-size:27px;line-height:28px;display:flex;align-items:flex-start;gap:8px}
.brand-dot{width:14px;height:14px;border-radius:50%;background:var(--white);margin-top:8px}
.social{left:584px;top:23px;display:flex;gap:3px}
.social span{width:16px;height:16px;background:#6d88c9;display:block}
.phone{left:645px;top:20px;display:flex;align-items:center;gap:5px;color:var(--lime);font-family:"Jost",sans-serif;font-size:18px}
.nav{right:140px;top:57px;display:flex;gap:14px;font-size:12px;color:var(--white)}
.nav .active{color:var(--lime)}
.rule{left:142px;top:91px;width:652px;border-top:1px dashed #6f86c6}
.tagline{left:142px;top:109px;font-family:"Jost",sans-serif;font-size:15.5px;color:var(--sky);letter-spacing:-.2px}
.video{left:142px;top:133px;width:383px;height:222px;background:linear-gradient(110deg,#3a3a3a,#cfcfcf 45%,#e9e9e9 60%,#2a2a2a)}
.play{left:303px;top:204px;width:61px;height:61px;border-radius:50%;background:rgba(40,40,40,.85)}
.pitch{left:540px;top:131px;width:255px;height:40px;background:var(--navy-deep);color:var(--lime);font-family:"Jost",sans-serif;font-size:14px;line-height:18px;text-align:center;padding-top:3px}
.benefits{left:543px;top:175px;width:250px;list-style:none;color:var(--white);font-size:9.6px;line-height:11.5px}
.benefits li{position:relative;padding-left:13px;margin-bottom:10.5px}
.benefits li::before{content:"›";position:absolute;left:0;top:-2px;font-size:13px;color:#c9d6f3}
.btn-register{left:556px;top:317px;width:146px;height:40px;background:var(--lime-btn);border:1px solid #c7e58c;color:#1f3c0a;font-weight:700;font-size:15px;display:flex;align-items:center;justify-content:center}

/* programs */
.programs{left:0;top:398px;width:934px;height:158px;background:linear-gradient(#ffffff,#dcdcdc)}
.hatch{left:0;top:536px;width:934px;height:20px;background:repeating-linear-gradient(45deg,#d3d3d3 0 1px,#e6e6e6 1px 3px)}
.sec-title{width:934px;left:0;text-align:center;font-family:"Jost",sans-serif;font-size:21.5px;font-weight:400}
.programs-title{top:414px;color:var(--grass)}
.programs-sub{top:452px;width:934px;text-align:center;font-size:9.6px;color:var(--navy)}
.prog{font-size:11.4px;color:#333;display:flex;align-items:center;gap:3px}
.prog::before{content:"";width:9px;height:9px;background:var(--navy);display:block}

/* reasons */
.reasons-title{top:584px;color:var(--navy)}
.reason{width:130px;text-align:center}
.reason h3{font-size:11.6px;font-weight:700;color:var(--navy);margin-bottom:6px}
.reason p{font-size:9.8px;line-height:14.6px;color:var(--grey-text)}
.badge{width:106px;height:106px}
.btn-join{left:384px;top:855px;width:165px;height:50px;background:linear-gradient(#3a58aa,#213a85);border:1px solid #1a2e6b;color:var(--white);font-family:"Jost",sans-serif;font-size:19px;display:flex;align-items:center;justify-content:center}

/* info band */
.band{left:0;top:924px;width:934px;height:188px;background:var(--leaf)}
.band h2{font-family:"Jost",sans-serif;font-weight:300;font-size:19px;color:var(--white)}
.small{font-size:9.8px;color:var(--leaf-dark);line-height:13.4px}
.field{width:169px;height:23px;background:#c8dd98;border:1px solid #b0cc70;font-size:9.6px;color:#4c5b2c;padding:5px 6px}
.btn-grey{width:118px;height:32px;background:linear-gradient(#fafafa,#d9d9d9);border:1px solid #bbb;border-radius:2px;font-size:11.5px;font-weight:600;color:#555;display:flex;align-items:center;justify-content:center}

/* footer */
.footer{left:0;top:1112px;width:934px;height:88px;background:var(--navy)}
.zig-up{left:0;top:1106px;width:934px;height:6px;background:
  linear-gradient(45deg,var(--navy) 50%,transparent 50%) 0 0/8px 6px,
  linear-gradient(-45deg,var(--navy) 50%,transparent 50%) 0 0/8px 6px;}
.foot-nav{left:140px;top:1129px;display:flex;gap:10px;font-size:10px;color:var(--white)}
.copy{left:140px;top:1145px;font-size:10px;color:var(--white)}
.copy b{font-weight:400;color:var(--sky)}
.follow{left:142px;top:1164px;font-size:10px;color:var(--white);display:flex;align-items:center;gap:4px}
.follow i{width:15px;height:15px;border-radius:50%;background:#8fbe3a;display:block}
.contact{left:648px;top:1132px;font-size:10px;line-height:14.5px;color:var(--white)}
</style>
</head>
<body>
<div class="page">

  <header class="abs hero"></header>
  <div class="abs zig-down" style="left:0;top:398px"></div>

  <div class="abs brand"><div>lumen<br>kinetics™</div><span class="brand-dot"></span></div>
  <div class="abs social" aria-label="Social links"><span></span><span></span><span></span></div>
  <div class="abs phone">
    <svg width="15" height="15" viewBox="0 0 16 16"><rect width="16" height="16" rx="3" fill="#a6d14a"/><path d="M5 3.5l1.6 2.4-1 1.1c.6 1.3 1.6 2.3 2.9 2.9l1.1-1 2.4 1.6-.7 1.8c-3.8-.3-6.9-3.4-7.2-7.2z" fill="#263f8a"/></svg>
    +61 (03) 5550 1234
  </div>
  <nav class="abs nav"><span class="active">Home</span><span>About us</span><span>Our Programs</span><span>Events</span><span>Products</span><span>Articles &amp; Resources</span><span>Contact us</span></nav>
  <div class="abs rule"></div>

  <p class="abs tagline">A NEW WAY OF THINKING TO CREATE A NEW WAY OF BEING.</p>
  <div class="abs video" role="img" aria-label="Video still: a trainer presenting at a whiteboard to a workshop participant"></div>
  <div class="abs play"><svg width="61" height="61" viewBox="0 0 61 61"><path d="M24 18l19 12.5L24 43z" fill="#fff"/></svg></div>

  <div class="abs pitch">Lumen Kinetics™ is for everyone. It's all<br>about Transformation and Skills for Life.</div>
  <ul class="abs benefits">
    <li>Improve your health and wellbeing</li>
    <li>Create a new fun and healthy culture</li>
    <li>Learn new ways to manage stress and create balance in your life</li>
    <li>Enhance your communication skills and strengthen your relationships</li>
    <li>Learn new ways to Transform and create all that you have ever wanted.</li>
  </ul>
  <div class="abs btn-register">REGISTER NOW</div>

  <section class="abs programs"></section>
  <div class="abs zig-down" style="left:0;top:398px"></div>
  <div class="abs hatch"></div>
  <h2 class="abs sec-title programs-title">TRAINING PROGRAMS</h2>
  <p class="abs programs-sub">Lumen Kinetics™ is a series of Development (Training) Programs that we deliver both for the General Public as well as Corporate Business.</p>
  <div class="abs prog" style="left:154px;top:473px">Programs for You</div>
  <div class="abs prog" style="left:358px;top:473px">Programs for Children and Schools</div>
  <div class="abs prog" style="left:606px;top:473px">Programs for Business</div>
  <div class="abs prog" style="left:154px;top:500px">Programs for Animals</div>
  <div class="abs prog" style="left:358px;top:500px">Programs for Community</div>
  <div class="abs prog" style="left:606px;top:500px">Programs for Practitioner</div>

  <h2 class="abs sec-title reasons-title">5 REASONS TO CHOOSE US</h2>

  <!-- badges -->
  <svg class="abs badge" style="left:142px;top:623px" viewBox="0 0 106 106"><circle cx="53" cy="53" r="48" fill="#8fbe3a"/><circle cx="53" cy="53" r="49" fill="none" stroke="#8fbe3a" stroke-width="6" stroke-dasharray="4 4"/><path d="M40 32h26v12c0 8-6 13-13 13s-13-5-13-13z M35 34h5v6c-3 0-5-2-5-6z M71 34h-5v6c3 0 5-2 5-6z M50 56h6v8h-6z M43 64h20v6H43z" fill="#fff"/></svg>
  <svg class="abs badge" style="left:278px;top:623px" viewBox="0 0 106 106"><circle cx="53" cy="53" r="48" fill="#8fbe3a"/><circle cx="53" cy="53" r="49" fill="none" stroke="#8fbe3a" stroke-width="6" stroke-dasharray="4 4"/><circle cx="40" cy="38" r="7" fill="#fff"/><circle cx="66" cy="38" r="7" fill="#fff"/><circle cx="53" cy="45" r="9" fill="#fff"/><path d="M28 60c0-8 6-12 12-12s7 3 7 3h12s2-3 7-3 12 4 12 12v6H28z M38 72c0-9 6-14 15-14s15 5 15 14v4H38z" fill="#fff"/></svg>
  <svg class="abs badge" style="left:414px;top:623px" viewBox="0 0 106 106"><circle cx="53" cy="53" r="48" fill="#8fbe3a"/><circle cx="53" cy="53" r="49" fill="none" stroke="#8fbe3a" stroke-width="6" stroke-dasharray="4 4"/><path d="M24 53c8-11 18-17 29-17s21 6 29 17c-8 11-18 17-29 17s-21-6-29-17z" fill="none" stroke="#fff" stroke-width="6"/><circle cx="53" cy="53" r="10" fill="#fff"/></svg>
  <svg class="abs badge" style="left:549px;top:623px" viewBox="0 0 106 106"><circle cx="53" cy="53" r="48" fill="#8fbe3a"/><circle cx="53" cy="53" r="49" fill="none" stroke="#8fbe3a" stroke-width="6" stroke-dasharray="4 4"/><path d="M32 70c0-22 16-32 40-32-2 22-14 34-34 30" fill="none" stroke="#fff" stroke-width="6" stroke-linecap="round"/><path d="M36 66c8-10 16-16 26-20" stroke="#fff" stroke-width="4" fill="none"/></svg>
  <svg class="abs badge" style="left:685px;top:623px" viewBox="0 0 106 106"><circle cx="53" cy="53" r="48" fill="#8fbe3a"/><circle cx="53" cy="53" r="49" fill="none" stroke="#8fbe3a" stroke-width="6" stroke-dasharray="4 4"/><rect x="33" y="33" width="40" height="40" rx="6" fill="#fff"/><path d="M49 40h8v9h9v8h-9v9h-8v-9h-9v-8h9z" fill="#8fbe3a"/></svg>

  <div class="abs reason" style="left:130px;top:744px"><h3>Leading Edge Programs</h3><p>Ourleading edge workshops and programs are designed and delivered in line with our philosophies</p></div>
  <div class="abs reason" style="left:266px;top:744px"><h3>Our Team</h3><p>Our executive team have over 40 years experience across major corporates as well as the health and wellness industries</p></div>
  <div class="abs reason" style="left:402px;top:744px"><h3>Our Vision</h3><p>Our vision is to teach and impart a new way of being and contributing to making the world a better place for all its inhabitants</p></div>
  <div class="abs reason" style="left:537px;top:744px"><h3>Fresh Approach</h3><p>We apply a unique and outside the box approach to everything we do. We are light on our feet and innovative in our thinking.</p></div>
  <div class="abs reason" style="left:673px;top:744px"><h3>Positive Difference</h3><p>We are here to make a positive difference by using our expertise to help business and individuals do what they do best</p></div>

  <div class="abs btn-join">JOIN US NOW</div>

  <section class="abs band"></section>
  <h2 class="abs heading" style="left:141px;top:937px;font-family:Jost,sans-serif;font-weight:300;font-size:19px;color:#fff">Upcoming Workshop</h2>
  <div class="abs" style="left:142px;top:966px;font-size:12.5px;font-weight:700;color:#2f5010">For You</div>
  <div class="abs" style="left:142px;top:984px;font-family:Jost,sans-serif;font-size:12.5px;color:#fff">June 2013</div>
  <div class="abs" style="left:142px;top:1002px;width:190px;font-size:11px;line-height:13px;color:#2f5010">Health &amp; Wellbeing - Sat 16 Jun - Melbourne, Australia</div>
  <div class="abs btn-grey" style="left:141px;top:1055px">Register Now</div>

  <h2 class="abs" style="left:371px;top:937px;font-family:Jost,sans-serif;font-weight:300;font-size:19px;color:#fff">Newsletter Subscription</h2>
  <div class="abs small" style="left:372px;top:968px">Subscribe for Free Newsletter</div>
  <div class="abs field" style="left:372px;top:992px">Your Name</div>
  <div class="abs field" style="left:372px;top:1018px">Your Email Id</div>
  <div class="abs btn-grey" style="left:372px;top:1055px">Subscribe Now</div>

  <h2 class="abs" style="left:602px;top:937px;font-family:Jost,sans-serif;font-weight:300;font-size:19px;color:#fff">Client Testimonial</h2>
  <div class="abs small" style="left:603px;top:970px;width:200px">This course went above and beyond what I expected.<br>This was an awesome course and very well suited to the Corporate World.<br>Head of Operations, Participant of Lumen Kinetics™ for Business</div>
  <div class="abs btn-grey" style="left:605px;top:1055px">More Testimonials</div>

  <footer class="abs footer"></footer>
  <div class="abs zig-up"></div>
  <nav class="abs foot-nav"><span>Home</span><span>About us</span><span>Our Programs</span><span>Events</span><span>Products</span><span>Articles &amp; Resources</span><span>Contact us</span></nav>
  <div class="abs copy"><b>Copyright © 2013 Lumen Kinetics</b> | PO Box 48, Harbour Lane, Vic 3999 Australia</div>
  <div class="abs follow">Follow us on <i></i><i></i><i></i></div>
  <div class="abs contact">Phone: +61 (3) 5550 1234<br>Mob: +61 (0) 400 555 018<br>Email: info@lumenkinetics.example.com</div>
</div>
</body>
</html>
```